Kelvar Systems Website

Website design for our company: Kelvar Systems.
The website should look fresh and IT focused. Please have a look at http://www.kelvarsystems.net.au/ for our current design. We want something fresh and new, professional looking, in WordPress so we can easily make changes.

Industry/Entity Type

It Company

```html
<!DOCTYPE html>
<html lang="en">
<head>
<meta charset="utf-8">
<title>Kelvar Systems</title>
<link href="https://fonts.googleapis.com/css2?family=Roboto:ital,wght@0,400;0,500;0,700;1,700;1,900&display=swap" rel="stylesheet">
<style>
:root{
  --green:#22a552;
  --green-dark:#1b8f46;
  --navy:#3b3e4c;
  --ink:#2b2d33;
  --muted:#9a9a9a;
  --light-bg:#f1f1f1;
  --footer:#2b2b2b;
  --partner-title:#2f2f2f;
  --partner-band:#4b4b4b;
  --white:#ffffff;
}
*{box-sizing:border-box;margin:0;padding:0}
html,body{width:1200px;height:2281px;overflow:hidden}
body{position:relative;background:var(--white);font-family:'Roboto',Arial,sans-serif;color:var(--ink)}
.abs{position:absolute}

/* header */
.site-header{position:absolute;left:0;top:0;width:1200px;height:122px;background:var(--white)}
.brand{position:absolute;left:101px;top:38px;display:flex;align-items:center;gap:14px}
.brand-dot{width:52px;height:52px;border-radius:50%;background:var(--green)}
.brand-name{font-size:30px;font-weight:700;color:var(--green)}
.follow{position:absolute;left:850px;top:18px;font-size:22px;font-weight:700;color:var(--green);letter-spacing:1px}
.social{position:absolute;top:12px;width:36px;height:36px;border-radius:50%;border:2px solid var(--ink)}
.ip{position:absolute;left:459px;top:66px;font-size:19px;font-weight:700;color:var(--green)}
.ip span{color:var(--ink);font-weight:500}
.search{position:absolute;left:761px;top:61px;width:234px;height:38px;background:var(--green);display:flex;align-items:center}
.search-field{margin-left:4px;width:182px;height:30px;background:var(--green-dark);color:var(--white);font-size:13px;line-height:30px;padding-left:8px}
.search-btn{width:44px;height:38px;display:flex;align-items:center;justify-content:center}
.badge{position:absolute;left:1005px;top:56px;width:99px;height:56px;background:var(--ink);border-radius:4px}

/* nav */
.main-nav{position:absolute;left:0;top:122px;width:1200px;height:58px;background:var(--navy)}
.main-nav a{position:absolute;top:0;height:58px;line-height:58px;color:var(--white);font-size:14px;font-weight:500;text-decoration:none}
.main-nav a.active{background:var(--green);padding:0 18px}

/* hero */
.hero{position:absolute;left:0;top:180px;width:1200px;height:416px;background:linear-gradient(135deg,#9c9c9c 0%,#d8d8d8 45%,#707070 100%)}
.hero-title{position:absolute;left:0;top:332px;width:1200px;text-align:center;color:var(--white);font-size:40px;font-weight:900;font-style:italic;letter-spacing:1px}

/* services */
.services{position:absolute;left:0;top:596px;width:1200px;height:325px;background:var(--light-bg)}
.svc-col{position:absolute;top:48px;width:300px}
.svc-num{position:absolute;left:0;top:0;width:49px;height:46px;background:var(--navy);color:var(--white);font-size:17px;line-height:46px;text-align:center}
.svc-head{position:absolute;left:66px;top:-2px;font-size:24px;line-height:27px;color:var(--ink);font-weight:500;text-transform:uppercase}
.svc-head span{display:block;color:var(--green);font-weight:400}
.svc-list{position:absolute;left:5px;top:98px;list-style:none}
.svc-list li{height:40px;font-size:13px;color:var(--muted);padding-left:26px;position:relative}
.svc-list li::before{content:"";position:absolute;left:0;top:5px;width:6px;height:6px;border-top:2px solid #777;border-right:2px solid #777;transform:rotate(45deg)}

/* features */
.features{position:absolute;left:0;top:921px;width:1200px;height:386px;background:linear-gradient(90deg,#4a4a4a 0%,#5d5d5d 60%,#6f6a64 100%)}
.feature{position:absolute;top:58px;width:320px;text-align:center;color:var(--white)}
.feature-icon{width:122px;height:122px;border-radius:50%;background:var(--green);margin:0 auto;display:flex;align-items:center;justify-content:center}
.feature h3{margin-top:24px;font-size:23px;font-weight:500}
.feature p{margin-top:8px;font-size:14px;font-weight:700;line-height:17px;padding:0 10px}

/* news */
.news-title{position:absolute;left:0;top:1338px;width:1200px;text-align:center;font-size:38px;font-weight:400;color:var(--ink)}
.news-item{position:absolute;top:1403px;width:315px;text-align:center}
.news-photo{width:315px;height:167px;background:linear-gradient(135deg,#8a8f96,#c9ccd0 55%,#6b6f75)}
.news-item h4{margin-top:20px;font-size:21px;font-weight:500;color:var(--green)}
.news-item p{margin-top:6px;font-size:12.5px;line-height:16px;color:var(--muted)}
.news-btn{position:absolute;left:490px;top:1700px;width:220px;height:48px;background:var(--green);color:var(--white);font-size:17px;font-weight:500;text-align:center;line-height:48px}

/* partners */
.partners-head{position:absolute;left:0;top:1789px;width:1200px;height:43px;background:var(--partner-title);color:var(--white);text-align:center;font-size:19px;font-weight:700;line-height:43px;letter-spacing:1px}
.partners-band{position:absolute;left:0;top:1832px;width:1200px;height:116px;background:var(--partner-band)}
.partner{position:absolute;top:38px;font-size:34px;font-weight:700;color:var(--white);transform:translateX(-50%)}

/* footer */
.site-footer{position:absolute;left:0;top:1948px;width:1200px;height:285px;background:var(--footer)}
.foot-col{position:absolute;top:46px}
.foot-col h5{font-size:16px;font-weight:500;color:var(--white);margin-bottom:14px}
.foot-col ul{list-style:none}
.foot-col li{font-size:12px;color:var(--muted);height:27px}
.foot-col li.current{color:var(--green)}
.contact-line{display:flex;align-items:center;gap:12px;height:33px;font-size:12px;color:var(--muted)}
.contact-line b{color:var(--white);font-weight:400;font-size:15px}
.contact-line .mail{color:var(--green)}
.foot-social{display:flex;gap:16px;margin-top:10px}
.foot-social i{width:16px;height:16px;border-radius:50%;background:#6b6b6b;display:block}
.remote-note{font-size:12px;color:var(--muted)}
.remote-input{margin-top:16px;width:254px;height:40px;background:var(--white);font-size:12px;color:var(--muted);line-height:40px;padding-left:10px}
.remote-btn{margin-top:13px;width:254px;height:35px;background:var(--green);color:var(--white);font-size:14px;font-weight:500;text-align:center;line-height:35px}
.copyright{position:absolute;left:0;top:2233px;width:1200px;height:48px;background:var(--green);color:var(--white);font-size:13px;text-align:center;line-height:48px}
</style>
</head>
<body>

<header class="site-header">
  <div class="brand"><div class="brand-dot"></div><div class="brand-name">Kelvar Systems</div></div>
  <div class="follow">FOLLOW US</div>
  <div class="social" style="left:986px"></div>
  <div class="social" style="left:1033px"></div>
  <div class="social" style="left:1080px"></div>
  <div class="ip">Your current IP- <span>xxx.xxx.xxx.xxx</span></div>
  <div class="search">
    <div class="search-field">Site Search</div>
    <div class="search-btn">
      <svg width="20" height="20" viewBox="0 0 20 20"><circle cx="8" cy="8" r="6" fill="none" stroke="#fff" stroke-width="2.5"/><line x1="12.5" y1="12.5" x2="18" y2="18" stroke="#fff" stroke-width="3"/></svg>
    </div>
  </div>
  <div class="badge"></div>
</header>

<nav class="main-nav">
  <a class="active" style="left:101px">HOME</a>
  <a style="left:188px">SUPPLIERS</a>
  <a style="left:294px">SERVICES</a>
  <a style="left:393px">SUPPORTS</a>
  <a style="left:500px">TESTIMONIALS</a>
  <a style="left:629px">CONTACT US</a>
  <a style="left:746px">ABOUT US</a>
</nav>

<section class="hero" role="img" aria-label="Photo of a hand on a computer mouse beside a laptop">
  <div class="hero-title">BEST COMPUTER REPAIR</div>
</section>

<section class="services">
  <div class="svc-col" style="left:129px">
    <div class="svc-num">01</div>
    <div class="svc-head">Home<span>Services</span></div>
    <ul class="svc-list"><li>Same Day In-Home Support</li><li>Certified Technicians</li><li>Virus &amp; Spyware Removal</li><li>Wireless Networking</li></ul>
  </div>
  <div class="svc-col" style="left:452px">
    <div class="svc-num">02</div>
    <div class="svc-head">Business<span>Services</span></div>
    <ul class="svc-list"><li>On-site Engineers</li><li>AD, Mail Server, SQL</li><li>Vendor Certified</li><li>Maintenance Contracts</li></ul>
  </div>
  <div class="svc-col" style="left:769px">
    <div class="svc-num">03</div>
    <div class="svc-head">Nationwide<span>IT Services</span></div>
    <ul class="svc-list"><li>Nationwide IT Workforce</li><li>OEM Hardware Installations</li><li>IT Project Management</li><li>Staff Augmentation</li></ul>
  </div>
</section>

<section class="features" role="img" aria-label="Background photo of a person working on a laptop">
  <div class="feature" style="left:111px">
    <div class="feature-icon"><svg width="44" height="40" viewBox="0 0 44 40"><rect x="3" y="3" width="38" height="25" fill="none" stroke="#fff" stroke-width="4"/><rect x="18" y="28" width="8" height="6" fill="#fff"/><rect x="12" y="34" width="20" height="3" fill="#fff"/></svg></div>
    <h3>Computer Repair</h3>
    <p>Lorem ipsum dolor sit amet, consectetuer adipiscing elit, sed diam nonummy nibh euismod tincidunt ut laoreet dolore magna aliquam erat volutpat.</p>
  </div>
  <div class="feature" style="left:441px">
    <div class="feature-icon"><svg width="40" height="40" viewBox="0 0 40 40"><circle cx="20" cy="20" r="17" fill="#fff"/><path d="M12 13c4 1 6 4 5 8s3 5 1 9M26 9c-2 3 1 6 4 6s3 6 0 8" fill="none" stroke="#22a552" stroke-width="3"/></svg></div>
    <h3>Internet Services</h3>
    <p>Lorem ipsum dolor sit amet, consectetuer adipiscing elit, sed diam nonummy nibh euismod tincidunt ut laoreet dolore magna aliquam erat volutpat.</p>
  </div>
  <div class="feature" style="left:779px">
    <div class="feature-icon"><svg width="26" height="42" viewBox="0 0 26 42"><rect x="2" y="2" width="22" height="38" rx="3" fill="none" stroke="#fff" stroke-width="3.5"/><circle cx="13" cy="34" r="2" fill="#fff"/></svg></div>
    <h3>Smartphone Repair</h3>
    <p>Lorem ipsum dolor sit amet, consectetuer adipiscing elit, sed diam nonummy nibh euismod tincidunt ut laoreet dolore magna aliquam erat volutpat.</p>
  </div>
</section>

<h2 class="news-title">Latest News</h2>
<article class="news-item" style="left:101px">
  <div class="news-photo" role="img" aria-label="Photo of a technician at a workbench"></div>
  <h4>Excepteur sint occaecat</h4>
  <p>Lorem ipsum dolor sit amet, consectetuer adipiscing elit, sed diam nonummy nibh euismod tincidunt ut laoreet dolore magna aliquam erat volutpat.</p>
</article>
<article class="news-item" style="left:441px">
  <div class="news-photo" role="img" aria-label="Photo of two people working at a computer"></div>
  <h4>Sunt in culpa qui officia</h4>
  <p>Lorem ipsum dolor sit amet, consectetuer adipiscing elit, sed diam nonummy nibh euismod tincidunt ut laoreet dolore magna aliquam erat volutpat.</p>
</article>
<article class="news-item" style="left:781px">
  <div class="news-photo" role="img" aria-label="Photo of an office team at their desks"></div>
  <h4>Cupidatat non proident</h4>
  <p>Lorem ipsum dolor sit amet, consectetuer adipiscing elit, sed diam nonummy nibh euismod tincidunt ut laoreet dolore magna aliquam erat volutpat.</p>
</article>
<div class="news-btn">See all news</div>

<div class="partners-head">BUSINESS PARTNERS</div>
<div class="partners-band">
  <span class="partner" style="left:167px">Norvane</span>
  <span class="partner" style="left:317px">Quellix</span>
  <span class="partner" style="left:510px">Stratel</span>
  <span class="partner" style="left:708px">Pellow</span>
  <span class="partner" style="left:962px">Vireon</span>
</div>

<footer class="site-footer">
  <div class="foot-col" style="left:101px">
    <h5>Navigation</h5>
    <ul><li class="current">Home</li><li>About</li><li>Services</li><li>News</li><li>Contacts</li></ul>
  </div>
  <div class="foot-col" style="left:254px">
    <h5>Categories</h5>
    <ul><li>Same Day In-Home Support</li><li>Certified Technicians</li><li>Virus &amp; Spyware Removal</li><li>Wireless Networking</li><li>On-site Engineers</li><li>AD, Mail Server, SQL</li></ul>
  </div>
  <div class="foot-col" style="left:487px">
    <h5>Contacts</h5>
    <div class="contact-line"><svg width="16" height="20" viewBox="0 0 16 20"><path d="M8 1a6 6 0 0 0-6 6c0 5 6 12 6 12s6-7 6-12a6 6 0 0 0-6-6z" fill="#fff"/><circle cx="8" cy="7" r="2.3" fill="#2b2b2b"/></svg>27 Harbour Lane Ashgrove 5042 Australia</div>
    <div class="contact-line"><svg width="16" height="18" viewBox="0 0 16 18"><path d="M3 1l3 4-2 2c1 3 3 5 6 6l2-2 4 3-2 3C7 17 0 10 1 3z" fill="#fff"/></svg>Call us: <b>+ 0885550147</b></div>
    <div class="contact-line"><svg width="20" height="14" viewBox="0 0 20 14"><rect x="1" y="1" width="18" height="12" fill="none" stroke="#22a552" stroke-width="2"/><path d="M1 1l9 7 9-7" fill="none" stroke="#22a552" stroke-width="2"/></svg><span class="mail">contact@kelvarsystems.net.au</span></div>
    <div class="foot-social"><i></i><i></i><i></i></div>
  </div>
  <div class="foot-col" style="left:847px">
    <h5>Remote Support</h5>
    <div class="remote-note">Enter your 6-digit code</div>
    <div class="remote-input">Enter your 6-digit code</div>
    <div class="remote-btn">Connect Now</div>
  </div>
</footer>
<div class="copyright">© 2014 Kelvar Systems. All Rights Reserved.</div>

</body>
</html>
```